Beautiful Customer Appreciation Gift Box Need Eye Catching Brochure

I need a brochure to include with small sample gift boxes that I send or give to companies who do door to door marketing of businesses, company reps, real estate designers and large companies looking for a unique customer appreciation gifts.

The brochure needs to capture the size variations and the limitless options for their budget and customization needs.

They are gift boxes that can be filled with cookies for the drug rep making an impression for the doc - after cookies are gone, the gift remains

At christmas, we fill them with baked goods and provide to each office. Every year as i visit the offices, they have last years gift box out as a decoration.

realtors can use them as a welcome to your new home gift filled with a bottle of wine and their papers left on the kitchen counter

We have had them used for baby shower gifts, kept later as a decoration.

that's the concept, i need it captured.
Marlow's Festive Nook is the current name
a tag line we came up with is It's all in the WRAPPINGS.
Updates

Project Deadline Extended
Reason: We are very close, I have my photoshoot tomorrow and I'd like to see and continue to tweek the current designs. I have pretty well deleted the designs we are not considering at this point. The others all have components we love. So I need a little more time and some tweaking to decide for sure.

Target Market(s)

the target is the company or individuals looking for gift giving options for clients and customers. From the door to door salesperson looking to make a splash or big impression to the large company looking for nice corporate gift ideas.

The concept of say goodbye to plain jane gift boxes that all look alike... Say goodbye to expensive gift wrap and bows that get thrown away in minutes.... and hello to a beautiful custom made gift box that will remain a decoration or keepsake box forever....

Industry/Entity Type

Retail

Font styles to use
Sans Serif
Script

Requirements
Must have
• IMPORTANT... I CAN and AM GETTING better pictures for the printing purposes. I'm looking more for the concept of the brochuure and layout design.
• I'd love to have it have some place holders for various pictures and descriptions - because each industry targets different people, I'd like to be able to change the front cover of the brochure with a picture of a box that targets that audience a little.
• For a real estate person... i might choose a beautiful centerpiece looking one... vs, the ob/gyn office, I might choose a baby one.
• I have some design skill, just 0 times and the programs have changed alot over the years, so this may go on to future work and a long design relationship as the company grows and changes. I do know photoshop and pagemaker from long ago so I should be able to drop in pics and text options. if we use compatible programs.
Nice to have
• would love to have some kind of background for the page - not just plain white background.
• i like angles and curves
Should not have
• boxy look.

```html
<!DOCTYPE html>
<html lang="en">
<head>
<meta charset="utf-8">
<title>Marlow's Festive Nook – Gift Box Brochure</title>
<link rel="stylesheet" href="https://fonts.googleapis.com/css2?family=Roboto:wght@400;700&family=Great+Vibes&display=swap">
<style>
  :root {
    --stage: #bfbfbf;
    --stage-label: #6f6f6f;
    --cream: #f8e4b9;
    --lilac: #d4acd4;
    --orchid: #b877bb;
    --plum-line: #9a4f9e;
    --plum: #7a1f6f;
    --white: #ffffff;
    --photo-pink: #d06aa8;
    --photo-green: #5f7a4a;
    --photo-wood: #7a5234;
  }
  * { box-sizing: border-box; margin: 0; padding: 0; }
  html, body { width: 1000px; height: 1200px; overflow: hidden; background: var(--stage); }
  body { position: relative; font-family: "Roboto", Arial, sans-serif; }

  .side-label {
    position: absolute; left: 92px; color: var(--stage-label);
    font: 400 44px/1 "Roboto", Arial, sans-serif; letter-spacing: 4px;
    transform: translate(-50%, -50%) rotate(-90deg); white-space: nowrap;
  }
  .side-label--outside { top: 305px; }
  .side-label--inside { top: 895px; }

  .sheet {
    position: absolute; left: 168px; width: 735px; height: 575px; overflow: hidden;
    background: var(--cream); box-shadow: 3px 4px 8px rgba(0,0,0,.35);
  }
  .sheet--outside { top: 10px; }
  .sheet--inside { top: 605px; }
  .sheet__waves { position: absolute; inset: 0; width: 735px; height: 575px; }

  .photo { position: absolute; border: 4px solid var(--white); }
  .photo--frame { border-radius: 34px; box-shadow: 0 0 0 2px var(--plum-line); }
  .photo--round { border-radius: 50%; border: 6px solid var(--plum); box-shadow: 0 0 0 3px var(--white); }
  .photo--flowers { background: radial-gradient(circle at 55% 55%, var(--photo-pink), #b8a0c8 45%, var(--photo-green) 85%); }
  .photo--box { background: radial-gradient(circle at 45% 55%, #c9a878, #3c3c7a 55%, var(--photo-green)); }
  .photo--pink-box { background: linear-gradient(180deg, #8a6a4a, #e6b8cc 45%, #e8a8c8); }
  .photo--blue-bloom { background: radial-gradient(circle at 45% 50%, #3f5fa8, #9bb8c8 45%, var(--photo-wood)); }
  .photo--violet-bloom { background: radial-gradient(circle at 50% 60%, #7a5fb0, #d8d0e8 45%, #8a8060); }
  .photo--book-box { background: linear-gradient(160deg, var(--photo-green), #6a5030 35%, #d8c8a0 65%, #3a3a3a); }

  .brand-name {
    position: absolute; left: 512px; top: 80px; width: 185px;
    color: var(--plum); font: 700 30px/1.15 "Roboto", Arial, sans-serif; text-align: center;
  }

  .block { position: absolute; width: 185px; color: var(--plum); }
  .block--narrow { width: 140px; }
  .block--keepsakes { width: 178px; }
  .block__title { font: 700 10.5px/1.25 "Roboto", Arial, sans-serif; text-transform: uppercase; margin-bottom: 10px; }
  .block__body { font: 400 7.4px/1.35 "Roboto", Arial, sans-serif; margin-bottom: 8px; }
  .block--light { color: var(--white); }

  .script { position: absolute; font-family: "Great Vibes", cursive; white-space: nowrap; }
  .script--tagline { left: 508px; top: 342px; font-size: 19px; color: var(--plum); transform: rotate(4deg); transform-origin: left center; }
  .script--gift { left: 630px; top: 488px; font-size: 24px; line-height: .9; color: var(--white); }

  .contact { position: absolute; left: 290px; top: 465px; width: 170px; color: var(--white); text-align: center; }
  .contact__title { font: 700 12px/1 "Roboto", Arial, sans-serif; margin-bottom: 12px; }
  .contact__phone { font: 700 16px/1 "Roboto", Arial, sans-serif; margin-bottom: 10px; }
  .contact__line { font: 400 10px/1.6 "Roboto", Arial, sans-serif; }
</style>
</head>
<body>
  <div class="side-label side-label--outside">OUTSIDE</div>
  <div class="side-label side-label--inside">INSIDE</div>

  <section class="sheet sheet--outside">
    <svg class="sheet__waves" viewBox="0 0 735 575" aria-hidden="true">
      <path fill="var(--lilac)" d="M330 0H735V45C600 30 470 60 330 105Z"/>
      <path fill="var(--orchid)" d="M330 105C470 62 600 34 735 48V60C600 48 470 78 330 120Z"/>
      <path fill="var(--orchid)" d="M0 430C200 455 430 420 735 345V575H0Z"/>
      <path fill="var(--plum-line)" d="M0 395C180 430 360 420 520 385C600 368 670 352 735 345V360C660 372 600 390 520 405C360 440 180 445 0 420Z"/>
      <path fill="var(--white)" d="M0 370C160 400 330 400 470 375C580 355 660 335 735 330V350C650 360 580 378 480 398C330 428 160 425 0 400Z"/>
      <path fill="var(--white)" d="M60 392C140 380 220 388 290 386C220 395 140 398 60 392Z"/>
    </svg>

    <div class="photo photo--frame photo--flowers" style="left:-4px;top:-4px;width:370px;height:234px" role="img" aria-label="Silk flower arrangement with a small angel figurine"></div>
    <div class="photo photo--round photo--box" style="left:307px;top:100px;width:136px;height:136px" role="img" aria-label="Decorated keepsake gift box filled with cookies"></div>

    <div class="brand-name">Marlow's Festive Nook</div>

    <div class="block" style="left:34px;top:266px">
      <h2 class="block__title">About our products</h2>
      <p class="block__body">Lorem ipsum dolor sit amet, consectetur adipiscing elit, sed do eiusmod tempor incididunt ut labore et dolore magna aliqua.</p>
      <p class="block__body">Ut enim ad minim veniam, quis nostrud exercitation ullamco laboris nisi ut aliquip ex ea commodo consequat.</p>
    </div>
    <div class="block block--keepsakes" style="left:278px;top:266px">
      <h2 class="block__title">Custom&nbsp; Keepsakes</h2>
      <p class="block__body">Say goodbye to plain jane gift boxes that all look alike... Say goodbye to expensive gift wrap and bows that get thrown away in minutes.... And hello to a beautiful custom made gift box that will remain a decoration or keepsake box forever....</p>
    </div>

    <div class="script script--tagline">Beautiful, Custom Made</div>

    <div class="contact">
      <h2 class="contact__title">CONTACT US</h2>
      <p class="contact__phone">555-014-2277</p>
      <p class="contact__line">e-mail: hello@marlowsnook.com</p>
      <p class="contact__line">web: marlowsfestivenook.com</p>
    </div>

    <div class="photo photo--round photo--box" style="left:502px;top:430px;width:100px;height:100px" role="img" aria-label="Keepsake gift box with cookies, open lid"></div>
    <div class="photo photo--round photo--box" style="left:623px;top:380px;width:84px;height:84px" role="img" aria-label="Keepsake gift box with cookies, side view"></div>
    <div class="script script--gift">Gift<br>&nbsp;&nbsp;Boxes</div>
  </section>

  <section class="sheet sheet--inside">
    <svg class="sheet__waves" viewBox="0 0 735 575" aria-hidden="true">
      <path fill="var(--lilac)" d="M0 0H735V35C520 20 260 60 0 100Z"/>
      <path fill="var(--orchid)" d="M0 100C260 58 520 28 735 42V55C520 42 260 75 0 118Z"/>
      <path fill="var(--orchid)" d="M0 395C200 418 400 410 735 365V575H0Z"/>
      <path fill="var(--plum-line)" d="M0 365C180 395 380 395 560 360L735 335V350L560 378C380 415 180 415 0 388Z"/>
      <path fill="var(--white)" d="M0 335C170 365 370 368 540 335L735 305V325L540 355C370 390 170 388 0 360Z"/>
    </svg>

    <div class="photo photo--frame photo--pink-box" style="left:47px;top:35px;width:140px;height:195px" role="img" aria-label="Pink keepsake box topped with roses and peonies"></div>
    <div class="photo photo--frame photo--blue-bloom" style="left:292px;top:35px;width:148px;height:195px" role="img" aria-label="Blue and cream silk flower arrangement"></div>
    <div class="photo photo--frame photo--violet-bloom" style="left:539px;top:35px;width:136px;height:195px" role="img" aria-label="Purple and white floral centerpiece on a book box"></div>

    <div class="block" style="left:31px;top:255px">
      <h2 class="block__title" style="margin-bottom:6px">Price<br>Product description</h2>
      <p class="block__body">Lorem ipsum dolor sit amet, consectetur adipiscing elit, sed do eiusmod tempor incididunt ut labore et dolore magna aliqua.</p>
    </div>
    <div class="block" style="left:277px;top:253px">
      <h2 class="block__title" style="margin-bottom:6px">Price<br>Product description</h2>
      <p class="block__body">Lorem ipsum dolor sit amet, consectetur adipiscing elit, sed do eiusmod tempor incididunt ut labore et dolore magna aliqua.</p>
    </div>
    <div class="block" style="left:522px;top:255px">
      <h2 class="block__title" style="margin-bottom:6px">Price<br>Product description</h2>
      <p class="block__body">Lorem ipsum dolor sit amet, consectetur adipiscing elit, sed do eiusmod tempor incididunt ut labore et dolore magna aliqua.</p>
    </div>

    <div class="block block--light" style="left:31px;top:446px">
      <h2 class="block__title" style="margin-bottom:8px">What your<br>budget can get you</h2>
      <p class="block__body">Lorem ipsum dolor sit amet, consectetur adipiscing elit, sed do eiusmod tempor incididunt ut labore et dolore magna aliqua.</p>
      <p class="block__body">Lorem ipsum dolor sit amet, consectetur adipiscing elit, sed do eiusmod tempor incididunt ut labore et dolore magna aliqua.</p>
    </div>
    <div class="block block--light block--narrow" style="left:277px;top:474px">
      <p class="block__body">Lorem ipsum dolor sit amet, consectetur adipiscing elit, sed do eiusmod tempor incididunt ut labore et dolore magna aliqua. Lorem ipsum dolor sit amet, consectetur adipiscing elit, sed do eiusmod tempor incididunt ut labore et dolore magna aliqua.</p>
    </div>

    <div class="photo photo--frame photo--book-box" style="left:425px;top:355px;width:320px;height:230px" role="img" aria-label="Open book-style keepsake box with greenery on a wooden table"></div>
    <div class="photo photo--round photo--box" style="left:357px;top:330px;width:128px;height:128px" role="img" aria-label="Keepsake gift box filled with cookies"></div>
  </section>
</body>
</html>
```